Design Large Inspirational Artwork with Long Quote

Design a large piece of art with a quote from Marcus Tillwright.

QUOTE
"The thing that's so interesting about being alive is that you're all in. No matter what you do, you're all in. This is gonna kill you, so I think you might as well play the most magnificent game you can while you're waiting. Because, do you have anything better to do? Why not pick the best thing possible that you could do? Because you're more powerful than you think, way more powerful than you think. I mean, God only knows what you are in the final analysis. You're blind to your own weaknesses, but you're also blind to your own strengths. How far could you take that if you stopped wasting time, and if you stopped lying, and if you oriented yourself to the highest possible good that you could conceive of and you committed to that? How much good could you do? Well, I would say: why don't you find out?"

SIZE
A high-resolution print size of 6' wide and 3' tall should provide ample space for both the quote and the accompanying artwork.

TYPOGRAPHY
Choose a bold, clean, and easily readable font for the quote. You could also experiment with different font sizes for certain words or phrases to emphasize their importance within the quote.

COLORS
Since the quote is thought-provoking and reflective, you might want to use a color palette that evokes a sense of introspection and depth. Consider using cool, calming colors like shades of blue, gray, or green. Alternatively, you can use a contrasting color scheme with a light background and dark text to make the quote stand out.

ARTWORK
Select / create / edit background artwork to complement the quote.
While a great design might be minimalistic and/or greyscale, I'd really like to see some full color options. This might be anything from photography or graphics inspired by the ideas in the text, to abstract colors or illustrations that feel like the sentiment expressed.
The art should capture your attention and encourage you to read the text. The art should be visually appealing, both at a distance and up close, regardless of whether the text is read.
Updates

Having trouble confirming the exact print size.

Still looking for printing solution and final size confirmation.

Target Market(s)

Personal, business, office

Industry/Entity Type

None

Font styles to use
Sans Serif
Script

Requirements
Must have
• Entire quote, legible text, modern design, attractive artwork, approx 6ft wide and 3ft tall
Nice to have
• Different font (sizes) for certain words or phrases to emphasize their importance within the quote.

```html
<!DOCTYPE html>
<html lang="en">
<head>
<meta charset="utf-8">
<title>All In — Inspirational Quote Artwork</title>
<link rel="stylesheet" href="https://fonts.googleapis.com/css2?family=Exo+2:wght@500;700&display=swap">
<style>
  :root {
    --ink: #111418;
    --accent: #1ea3cc;
    --closing: #ffffff;
    --mist-light: #e6eaee;
    --mist-mid: #b9c6d0;
    --lake: #6f8798;
    --lake-deep: #3f5566;
  }
  html, body {
    margin: 0;
    padding: 0;
    width: 1200px;
    height: 603px;
    overflow: hidden;
  }
  .artwork {
    position: relative;
    width: 1200px;
    height: 603px;
    overflow: hidden;
    font-family: "Exo 2", sans-serif;
  }
  .backdrop {
    position: absolute;
    inset: 0;
    background:
      radial-gradient(ellipse 55% 45% at 18% 20%, var(--mist-light) 0%, transparent 70%),
      radial-gradient(ellipse 40% 50% at 85% 55%, var(--lake-deep) 0%, transparent 75%),
      radial-gradient(ellipse 35% 30% at 10% 85%, #5b5f63 0%, transparent 80%),
      linear-gradient(180deg, var(--mist-light) 0%, var(--mist-mid) 40%, var(--lake) 75%, var(--lake-deep) 100%);
  }
  .quote {
    position: absolute;
    left: 236px;
    top: 27px;
    width: 800px;
    margin: 0;
    text-align: center;
    color: var(--ink);
    font-weight: 500;
    font-size: 23.5px;
    line-height: 31.7px;
  }
  .quote .line { display: block; white-space: nowrap; }
  .quote .emphasis { color: var(--accent); }
  .closing {
    position: absolute;
    left: 236px;
    top: 540px;
    width: 800px;
    margin: 0;
    text-align: center;
    color: var(--closing);
    font-weight: 700;
    font-size: 35px;
    line-height: 44px;
    white-space: nowrap;
  }
</style>
</head>
<body>
<main class="artwork">
  <div class="backdrop" role="img" aria-label="Misty mountain fjord landscape with a lone hiker in a red jacket standing on a rock ledge above the water"></div>
  <p class="quote">
    <span class="line">The thing that's so interesting about being alive is that you're all in.</span>
    <span class="line">No matter what you do, you're all in.</span>
    <span class="line">This is gonna kill you, so I think you might as well play</span>
    <span class="line">the most magnificent game you can while you're waiting.</span>
    <span class="line">Because, do you have anything better to do?</span>
    <span class="line">Why not pick the best thing possible that you could do?</span>
    <span class="line">Because you're more powerful than you think,</span>
    <span class="line">way more powerful than you think.</span>
    <span class="line emphasis">I mean, God only knows what you are in the final analysis.</span>
    <span class="line">You're blind to your own weaknesses,</span>
    <span class="line">but you're also blind to your own strengths.</span>
    <span class="line">How far could you take that if you stopped wasting time,</span>
    <span class="line">and if you stopped lying, and if you oriented yourself</span>
    <span class="line">to the highest possible good that</span>
    <span class="line">you could conceive of and you committed to that?</span>
    <span class="line">How much good could you do?</span>
  </p>
  <p class="closing">Well, I would say: why don't you find out?</p>
</main>
</body>
</html>
```